we are launching a Velmora Jest Room Chanel on Pim Ruz along with other social platforms and we need to create 6 "coming soon" post for Pim Ruz, QB etc, we need picture of famous trending comedians on the post announcing the launch of Velmora Jest Room social page. This page will host special Live Comedy shows, Trending comedians, Behind the scenes access to your favorite content creators, viral funny content and vines. while creating a theme to induce people to Follow, Subscribe, and turn those notifications on.

```html
<!DOCTYPE html>
<html lang="en">
<head>
<meta charset="utf-8">
<title>Velmora Jest Room — Coming Soon</title>
<link rel="stylesheet" href="https://fonts.googleapis.com/css2?family=Poppins:wght@400;500;800;900&display=swap">
<style>
  :root {
    --stage: #c8c8c8;
    --paper: #ffffff;
    --violet: #7043e6;
    --violet-ink: #5014e0;
    --sun: #ffe31c;
    --ink: #1b1533;
    --navy: #1d2438;
    --navy-soft: #2f3a58;
  }
  * { margin: 0; padding: 0; box-sizing: border-box; }
  html, body { width: 1200px; height: 1156px; overflow: hidden; }
  body { background: var(--stage); font-family: 'Poppins', sans-serif; position: relative; }

  .post {
    position: absolute; left: 126px; top: 104px;
    width: 949px; height: 949px; overflow: hidden; background: var(--paper);
  }
  .post > * { position: absolute; }

  .doodle-field { left: 0; top: 0; width: 480px; height: 949px;
    background: linear-gradient(160deg, #f4f4f6 0%, #ececef 50%, #f6f6f8 100%); }
  .violet-sheet, .torn-band, .marks { left: 0; top: 0; width: 949px; height: 949px; }

  .performers-photo {
    left: 196px; top: 336px; width: 640px; height: 640px;
    border: 8px solid var(--violet); border-bottom: 0;
    border-radius: 48px 48px 0 0;
    background: linear-gradient(170deg, var(--navy-soft) 0%, var(--navy) 60%, #151b2b 100%);
  }

  .headline { font-weight: 900; line-height: 1; letter-spacing: -1px; white-space: nowrap; }
  .headline--first { left: 118px; top: 108px; font-size: 74px; color: var(--violet-ink); transform: rotate(-3deg); transform-origin: left bottom; }
  .headline--second { left: 520px; top: 84px; font-size: 80px; color: var(--paper); transform: rotate(-3deg); transform-origin: left bottom; }
  .headline--third { left: 250px; top: 208px; font-size: 132px; color: var(--violet-ink); transform: rotate(-4deg); transform-origin: left bottom; }

  .launch-box {
    left: 128px; top: 718px; width: 730px; height: 104px; background: var(--paper);
    display: flex; align-items: center; justify-content: center;
  }
  .launch-box span { font-weight: 900; font-size: 96px; color: var(--violet-ink); letter-spacing: -2px; line-height: 1; }

  .action { top: 842px; height: 46px; border-radius: 23px; display: flex; align-items: center; justify-content: center; gap: 8px;
    font-size: 20px; font-weight: 400; color: var(--ink); white-space: nowrap; }
  .action--follow { left: 102px; width: 134px; background: var(--paper); }
  .action--subscribe { left: 258px; width: 168px; background: var(--paper); }
  .action--alerts { left: 441px; width: 411px; background: var(--sun); font-size: 23px; }

  .reaction { border-radius: 50%; }
  .reaction--warm { background: radial-gradient(circle at 40% 35%, #ffd23a, #f7a21b 70%, #e98a10); filter: blur(1px); }
  .reaction--heart { background: radial-gradient(circle at 40% 35%, #b06cf0, #7a2ad6 70%); }
</style>
</head>
<body>
<main class="post">
  <div class="doodle-field" role="img" aria-label="Faint hand-drawn cartoon face doodle pattern"></div>

  <svg class="violet-sheet" viewBox="0 0 949 949" aria-hidden="true">
    <path fill="var(--violet)" d="M470 0 L949 0 L949 949 L470 949 L478 880 L470 800 L478 740 L468 660 L474 560 L466 470 L474 380 L468 300 L476 220 L468 140 L476 60 Z"/>
  </svg>

  <svg class="torn-band" viewBox="0 0 949 949" aria-hidden="true">
    <path fill="#ffffff" d="M190 206 L480 196 L800 156 L812 164 L805 240 L818 320 L812 390 L822 396 L700 402 L480 416 L300 424 L210 410 L196 330 L200 260 Z"/>
    <path fill="var(--sun)" d="M200 212 L480 204 L792 168 L796 240 L806 318 L800 386 L700 392 L480 404 L302 412 L214 398 L206 330 L210 262 Z"/>
  </svg>

  <div class="performers-photo" role="img" aria-label="Photo of two laughing comedians in dark blazers, one holding a microphone, the other pointing forward"></div>

  <p class="headline headline--first">VELMORA</p>
  <p class="headline headline--second">JEST</p>
  <p class="headline headline--third">ROOM</p>

  <svg class="marks" viewBox="0 0 949 949" aria-hidden="true">
    <g stroke="#ffffff" stroke-width="4" stroke-linecap="round">
      <line x1="858" y1="428" x2="890" y2="414"/>
      <line x1="856" y1="454" x2="892" y2="452"/>
      <line x1="854" y1="482" x2="886" y2="490"/>
      <line x1="852" y1="506" x2="882" y2="520"/>
    </g>
    <g stroke="var(--violet-ink)" stroke-width="4" stroke-linecap="round">
      <line x1="142" y1="576" x2="178" y2="586"/>
      <line x1="138" y1="604" x2="174" y2="606"/>
      <line x1="140" y1="632" x2="176" y2="626"/>
      <line x1="154" y1="660" x2="182" y2="646"/>
    </g>
  </svg>

  <div class="reaction reaction--warm" style="left:-6px;top:588px;width:86px;height:86px" role="img" aria-label="Blurred heart-eyes reaction emoji"></div>
  <div class="reaction reaction--warm" style="left:874px;top:540px;width:110px;height:110px" role="img" aria-label="Laughing reaction emoji"></div>
  <div class="reaction reaction--warm" style="left:896px;top:740px;width:66px;height:66px" role="img" aria-label="Small blurred laughing reaction emoji"></div>
  <div class="reaction reaction--heart" style="left:920px;top:212px;width:64px;height:64px" role="img" aria-label="Heart reaction badge"></div>
  <div class="reaction reaction--heart" style="left:-20px;top:824px;width:52px;height:64px" role="img" aria-label="Heart reaction badge"></div>
  <div class="reaction reaction--heart" style="left:74px;top:540px;width:30px;height:30px" role="img" aria-label="Small heart reaction badge"></div>

  <div class="launch-box"><span>COMING SOON</span></div>

  <div class="action action--follow">
    <svg width="24" height="24" viewBox="0 0 24 24" aria-hidden="true">
      <path d="M3 13 L19 5 L13 21 L11 14 Z" fill="var(--violet-ink)"/>
      <g stroke="var(--violet-ink)" stroke-width="1.6" stroke-linecap="round"><line x1="20" y1="2" x2="20" y2="0.5"/><line x1="22" y1="5" x2="23.5" y2="4"/><line x1="16" y1="2" x2="15" y2="0.8"/></g>
    </svg>
    <span>FOLLOW</span>
  </div>
  <div class="action action--subscribe">
    <svg width="20" height="22" viewBox="0 0 20 22" aria-hidden="true">
      <path d="M10 2 C5.5 2 4 6 4 10 L4 14 L2 17 L18 17 L16 14 L16 10 C16 6 14.5 2 10 2 Z" fill="var(--violet-ink)"/>
      <circle cx="10" cy="19.5" r="2.2" fill="var(--violet-ink)"/>
    </svg>
    <span>SUBSCRIBE</span>
  </div>
  <div class="action action--alerts"><span>Turn those notifications on</span></div>
</main>
</body>
</html>
```